office stationary for pr
pr biz stationery
Creative Brief
Simple
Adaeze Nnorom
22 orin lane westbrook estate off kavel road pelmar
annorom@pelvora.com
www.pelvora.com
the logo should be used at the back of the business card

```html
<!DOCTYPE html>
<html lang="en">
<head>
<meta charset="utf-8">
<title>Pelvora Stationery</title>
<link href="https://fonts.googleapis.com/css2?family=Open+Sans:wght@400;600&display=swap" rel="stylesheet">
<style>
  :root {
    --backdrop: #ededed;
    --paper: #ffffff;
    --ink: #5a5a5a;
    --ink-soft: #8c8c8c;
    --rule: #9a9a9a;
    --accent: #39a9dc;
    --navy-deep: #0d2b4a;
    --navy: #1f5a86;
    --shadow: 0 2px 6px rgba(0,0,0,.18);
  }
  * { box-sizing: border-box; margin: 0; padding: 0; }
  html, body { width: 1200px; height: 866px; overflow: hidden; }
  body {
    background: var(--backdrop);
    font-family: "Open Sans", Arial, sans-serif;
    color: var(--ink);
    position: relative;
  }
  .sheet { position: absolute; background: var(--paper); box-shadow: var(--shadow); }

  .brand { position: absolute; display: flex; align-items: flex-start; gap: 4px; }
  .brand-dot { width: 8px; height: 8px; border-radius: 50%; background: var(--accent); margin-top: 2px; }
  .brand-name { font-weight: 400; color: var(--ink-soft); line-height: 1; }

  .rule { position: absolute; height: 1px; background: var(--rule); }

  .contact { position: absolute; font-size: 6.5px; line-height: 1.55; color: var(--ink); white-space: nowrap; }
  .contact .web { font-weight: 600; }

  /* Letterhead */
  .letterhead { left: 10px; top: 36px; width: 513px; height: 816px; }
  .letterhead .brand { left: 26px; top: 32px; }
  .letterhead .brand-name { font-size: 30px; }
  .letterhead .rule { left: 134px; right: 18px; top: 67px; }
  .letterhead .contact { left: 28px; top: 80px; }

  /* Business card front */
  .card-front { left: 607px; top: 62px; width: 223px; height: 147px; }
  .card-front .brand { left: 12px; top: 40px; }
  .card-front .brand-name { font-size: 20px; }
  .card-front .divider { position: absolute; left: 106px; top: 30px; width: 1px; height: 94px; background: var(--rule); }
  .card-front .holder { position: absolute; left: 114px; top: 18px; font-size: 8px; font-weight: 600; color: var(--navy-deep); }
  .card-front .contact { left: 114px; top: 42px; font-size: 5.5px; }

  /* Business card back */
  .card-back {
    left: 842px; top: 62px; width: 207px; height: 147px;
    background: radial-gradient(ellipse at 60% 35%, var(--navy) 0%, var(--navy-deep) 85%);
  }
  .card-back .brand { left: 50%; top: 50%; transform: translate(-50%, -50%); }
  .card-back .brand-name { font-size: 26px; color: #ffffff; }

  /* Envelope front */
  .envelope-front { left: 559px; top: 233px; width: 627px; height: 283px; }
  .envelope-front .brand { left: 22px; top: 12px; }
  .envelope-front .brand-name { font-size: 30px; }
  .envelope-front .rule { left: 132px; right: 10px; top: 46px; }
  .envelope-front .contact { left: 24px; top: 58px; }

  /* Envelope back */
  .envelope-back { left: 559px; top: 538px; width: 627px; height: 290px; overflow: hidden; }
  .envelope-back svg { position: absolute; right: 0; top: 0; }
  .flap-web {
    position: absolute; right: 26px; top: 50%;
    transform: translateY(-50%) rotate(90deg); transform-origin: center;
    font-size: 6px; color: #ffffff; letter-spacing: .3px; white-space: nowrap;
  }
</style>
</head>
<body>

  <section class="sheet letterhead" aria-label="Letterhead">
    <div class="brand"><span class="brand-name">Pelvora</span><span class="brand-dot"></span></div>
    <div class="rule"></div>
    <div class="contact">
      22 orin lane<br>
      westbrook estate<br>
      off kavel road pelmar<br>
      Phone: +234 809 555 0142<br>
      Email: annorom@pelvora.com<br>
      Website: <span class="web">www.pelvora.com</span>
    </div>
  </section>

  <section class="sheet card-front" aria-label="Business card front">
    <div class="brand"><span class="brand-name">Pelvora</span><span class="brand-dot"></span></div>
    <div class="divider"></div>
    <div class="holder">Adaeze Nnorom</div>
    <div class="contact">
      22 orin lane<br>
      westbrook estate<br>
      off kavel road pelmar<br>
      Mobile: +234 817 555 0196<br>
      Email: annorom@pelvora.com<br>
      Website: <span class="web">www.pelvora.com</span>
    </div>
  </section>

  <section class="sheet card-back" aria-label="Business card back">
    <div class="brand"><span class="brand-name">Pelvora</span><span class="brand-dot"></span></div>
  </section>

  <section class="sheet envelope-front" aria-label="Envelope front">
    <div class="brand"><span class="brand-name">Pelvora</span><span class="brand-dot"></span></div>
    <div class="rule"></div>
    <div class="contact">
      22 orin lane<br>
      westbrook estate<br>
      off kavel road pelmar<br>
      Phone: +234 809 555 0142<br>
      Email: annorom@pelvora.com<br>
      Website: <span class="web">www.pelvora.com</span>
    </div>
  </section>

  <section class="sheet envelope-back" aria-label="Envelope back">
    <svg width="72" height="290" viewBox="0 0 72 290" aria-hidden="true">
      <defs>
        <linearGradient id="flapShade" x1="0" y1="0" x2="1" y2="0">
          <stop offset="0" stop-color="#1f5a86"/>
          <stop offset="1" stop-color="#0d2b4a"/>
        </linearGradient>
      </defs>
      <path d="M72 0 H14 Q0 0 0 22 V268 Q0 290 14 290 H72 Z" fill="url(#flapShade)"/>
    </svg>
    <div class="flap-web">www.pelvora.com</div>
  </section>

</body>
</html>
```